Glamour By Tavi

I am a makeup artist looking for professional looking double sided business card. I would like to create a logo and incorporate a set of eyes as the periods above the name "Tavi" on the card.

front of card: Logo "Glamour by Tavi" written across diagonal (bottom left to top right)

Back of card:
1) Professional makeup artist serving New York & New Jersey (or similar to this text)
2) 917-555-0148
3) glamourbytavi@mailcove.com

Industry/Entity Type

Business

```html
<!DOCTYPE html>
<html lang="en">
<head>
<meta charset="utf-8">
<title>Glamour by Tavi — Business Card</title>
<link rel="stylesheet" href="https://fonts.googleapis.com/css2?family=Gilda+Display&family=Josefin+Sans:wght@400;600&display=swap">
<style>
  :root {
    --canvas: #ffffff;
    --card: #000000;
    --ink: #ffffff;
    --sky: #29a9e1;
    --teal: #14a79a;
    --leaf: #2bb673;
  }
  * { margin: 0; padding: 0; box-sizing: border-box; }
  html, body {
    width: 1200px;
    height: 1000px;
    overflow: hidden;
    background: var(--canvas);
  }
  .sheet {
    position: relative;
    width: 1200px;
    height: 1000px;
  }
  .card {
    position: absolute;
    width: 822px;
    height: 471px;
    background: var(--card);
    border-radius: 14px;
    color: var(--ink);
    overflow: hidden;
  }
  .card--front { left: 205px; top: 20px; }
  .card--back { left: 203px; top: 513px; }

  /* Front: diagonal name with brush stripe */
  .stripe {
    position: absolute;
    left: 0;
    top: 0;
    width: 822px;
    height: 471px;
  }
  .wordmark {
    position: absolute;
    left: 418px;
    top: 222px;
    display: flex;
    align-items: center;
    gap: 20px;
    white-space: nowrap;
    transform: translate(-50%, -50%) rotate(-24.4deg);
  }
  .wordmark__dot {
    flex: none;
    width: 24px;
    height: 24px;
    border-radius: 50%;
    background: var(--sky);
  }
  .wordmark__name {
    font-family: "Gilda Display", serif;
    font-size: 98px;
    font-weight: 400;
    line-height: 1;
    color: var(--ink);
  }

  /* Back */
  .eyes-art {
    position: absolute;
    left: 212px;
    top: 47px;
    width: 410px;
    height: 165px;
    border-radius: 6px;
    background: linear-gradient(180deg, var(--teal) 0%, var(--sky) 55%, var(--leaf) 100%);
    opacity: 0.85;
  }
  .details__line {
    position: absolute;
    left: 0;
    right: 0;
    text-align: center;
    line-height: 1;
    transform: translateY(-50%);
  }
  .details__title {
    top: 262px;
    font-family: "Gilda Display", serif;
    font-size: 50px;
  }
  .details__area {
    top: 311px;
    font-family: "Josefin Sans", sans-serif;
    font-weight: 600;
    font-size: 30px;
    font-variant: small-caps;
    letter-spacing: 6px;
  }
  .details__phone {
    top: 350px;
    font-family: "Gilda Display", serif;
    font-size: 36px;
  }
  .details__email {
    top: 395px;
    font-family: "Gilda Display", serif;
    font-size: 34px;
  }
</style>
</head>
<body>
  <main class="sheet">
    <section class="card card--front" aria-label="Card front">
      <svg class="stripe" viewBox="0 0 822 471" aria-hidden="true">
        <polygon points="150,438 800,144 803,148 160,437" fill="var(--ink)"/>
        <polygon points="172,440 805,150 795,158 180,441" fill="var(--sky)"/>
      </svg>
      <div class="wordmark">
        <span class="wordmark__dot" aria-hidden="true"></span>
        <span class="wordmark__name">Glamour by Tavi</span>
      </div>
    </section>

    <section class="card card--back" aria-label="Card back">
      <div class="eyes-art" role="img" aria-label="Illustration of a pair of stylised blue and green made-up eyes with swirls above"></div>
      <p class="details__line details__title">Professional Makeup Artist</p>
      <p class="details__line details__area">Serving New York &amp; New Jersey</p>
      <p class="details__line details__phone">917-555-0148</p>
      <p class="details__line details__email">glamourbytavi@mailcove.com</p>
    </section>
  </main>
</body>
</html>
```